Sudden Tides "Lantern Road" New Single Cover

Create cover artwork for the band Sudden Tides' new single "Lantern Road" being released early 2020. Style, font and graphics to be consistent with band's previous releases and overall brand identity. Visit www.suddentidesband.example and our Spotify page https://music.example.net/artist/7QzWpLx3RtVnKd8e2YbHcJ?si=MUrTgKa4PLe7skvWq2AmZd to view our previous releases and overall brand identity. Some examples attached as well. We are looking for someone to work with on future projects as well.

Lyrics are here: https://docs.example.org/document/d/3KTp9wrn_2ZQa8eXb4Lo_fimH7C5m83Jz4Pd70hrtVcA/edit

Music is here: https://audiostream.example.com/suddentides/lantern-road/s-pzkwa

Font styles to use
Sans Serif

Colors

Designer to choose colors to be used in the design.

Requirements
Must have
• Must be consistent with current brand identity and with prior album / single art.

```html
<!DOCTYPE html>
<html lang="en">
<head>
<meta charset="utf-8">
<title>Sudden Tides – Lantern Road</title>
<link rel="stylesheet" href="https://fonts.googleapis.com/css2?family=Open+Sans:wght@600;800&display=swap">
<style>
  :root {
    --stage: #5f5f5f;
    --teal: #16a6ab;
    --sun: #f2a91c;
    --navy: #1d2c5a;
    --white: #ffffff;
    --pattern-soft: rgba(242, 169, 28, 0.38);
    --pattern-fade: rgba(242, 169, 28, 0.22);
  }
  * { box-sizing: border-box; margin: 0; padding: 0; }
  html, body {
    width: 1200px;
    height: 793px;
    overflow: hidden;
    background: var(--stage);
  }
  .canvas {
    position: relative;
    width: 1200px;
    height: 793px;
    background: var(--stage);
  }
  .cover {
    position: absolute;
    left: 274px;
    top: 70px;
    width: 652px;
    height: 654px;
    background: var(--teal);
    font-family: "Open Sans", Arial, sans-serif;
  }
  .pattern {
    position: absolute;
    left: 81px;
    width: 490px;
    height: 199px;
    border-radius: 99px;
    background: linear-gradient(90deg, var(--pattern-soft), var(--pattern-fade), var(--pattern-soft));
  }
  .pattern--top { top: 44px; }
  .pattern--bottom { top: 339px; }
  .title {
    position: absolute;
    left: 0;
    right: 0;
    top: 250px;
    display: flex;
    justify-content: center;
    align-items: baseline;
    gap: 10px;
    line-height: 1;
    font-weight: 800;
  }
  .title__main {
    color: var(--sun);
    font-size: 74px;
    letter-spacing: -1px;
  }
  .title__tail {
    color: var(--navy);
    font-size: 50px;
  }
  .band-name {
    position: absolute;
    left: 0;
    right: 0;
    top: 562px;
    text-align: center;
    color: var(--white);
    font-weight: 600;
    font-size: 16px;
    line-height: 24px;
    letter-spacing: 3px;
    text-transform: uppercase;
  }
</style>
</head>
<body>
  <main class="canvas">
    <section class="cover">
      <div class="pattern pattern--top" role="img" aria-label="Two rows of five yellow outline smiley circles"></div>
      <h1 class="title">
        <span class="title__main">LANTERN</span>
        <span class="title__tail">ROAD</span>
      </h1>
      <div class="pattern pattern--bottom" role="img" aria-label="Two rows of five yellow outline smiley circles"></div>
      <p class="band-name">Sudden<br>Tides</p>
    </section>
  </main>
</body>
</html>
```